Professional & attention grabbing.

A business card design, front and back. I already have a logo I will attach, but I am open to something new as well.
Things to include:
Name:
Title:
Phone:
Email:
Wanting something that is professional but attention grabbing.
Also we do a lot of work using drones on natural gas pipelines (leading the future)if you want to include any of that. I'm open to ideas.
Target Market(s)
Natural gas transmission industry / greenhouse gas mitigation industry
Industry/Entity Type
Business
Contact Information for Business Card
All details have been conveyed above.
Colors
Designer to choose colors to be used in the design.
Look and feel
Each slider illustrates characteristics of the customer's brand and the style your logo design should communicate.

```html
<!DOCTYPE html>
<html lang="en">
<head>
<meta charset="utf-8">
<title>KV Field Inspections – Business Card</title>
<link rel="stylesheet" href="https://fonts.googleapis.com/css2?family=Roboto+Condensed:wght@400;700&display=swap">
<style>
  :root {
    --backdrop: #ecebe8;
    --card-white: #ffffff;
    --charcoal: #2a2c29;
    --slate: #3b3e40;
    --ink: #333333;
    --signal-red: #c4232a;
    --card-shadow: 0 10px 24px rgba(0, 0, 0, 0.18);
  }
  html, body {
    margin: 0;
    padding: 0;
    width: 1200px;
    height: 1000px;
    overflow: hidden;
    background: var(--backdrop);
    font-family: "Roboto Condensed", "Arial Narrow", sans-serif;
  }
  .canvas {
    position: relative;
    width: 1200px;
    height: 1000px;
  }
  .card {
    position: absolute;
    width: 620px;
    height: 354px;
    box-shadow: var(--card-shadow);
    overflow: hidden;
  }
  .card--front {
    left: 170px;
    top: 110px;
    background: var(--card-white);
  }
  .card--back {
    left: 410px;
    top: 530px;
    background: linear-gradient(135deg, var(--slate) 0%, var(--charcoal) 60%);
  }
  .back-band {
    position: absolute;
    top: 0;
    right: 0;
    width: 110px;
    height: 100%;
    background: var(--signal-red);
  }
  .brand {
    position: absolute;
    left: 44px;
    top: 150px;
    display: flex;
    align-items: center;
    gap: 10px;
  }
  .brand-square {
    width: 22px;
    height: 22px;
    background: var(--signal-red);
  }
  .brand-name {
    font-weight: 700;
    font-size: 22px;
    letter-spacing: 0.5px;
    color: var(--ink);
    text-transform: uppercase;
  }
  .identity {
    position: absolute;
    left: 300px;
    top: 70px;
  }
  .identity-name {
    margin: 0;
    font-weight: 700;
    font-size: 30px;
    line-height: 1;
    color: var(--ink);
    letter-spacing: 0.3px;
  }
  .identity-name .surname { color: var(--signal-red); }
  .identity-title {
    margin: 6px 0 0;
    font-weight: 400;
    font-size: 19px;
    color: var(--ink);
  }
  .contact-list {
    position: absolute;
    left: 330px;
    top: 205px;
    margin: 0;
    padding: 0;
    list-style: none;
    font-size: 15px;
    color: var(--ink);
    letter-spacing: 0.3px;
  }
  .contact-item {
    display: flex;
    align-items: flex-start;
    gap: 10px;
    margin-bottom: 9px;
    line-height: 1.15;
  }
  .contact-icon {
    width: 15px;
    height: 15px;
    flex: none;
    fill: var(--ink);
  }
</style>
</head>
<body>
<main class="canvas">

  <section class="card card--front" aria-label="Business card front">
    <div class="brand">
      <span class="brand-square"></span>
      <span class="brand-name">KV Field Inspections</span>
    </div>

    <div class="identity">
      <h1 class="identity-name">JOHN <span class="surname">DOE</span></h1>
      <p class="identity-title">Manager</p>
    </div>

    <ul class="contact-list">
      <li class="contact-item">
        <svg class="contact-icon" viewBox="0 0 16 16" aria-hidden="true"><path d="M2 5c0-2 2-3 6-3s6 1 6 3v1h-3V5H5v1H2zM4 7h8l2 6H2z"/></svg>
        <span>123 456 789</span>
      </li>
      <li class="contact-item">
        <svg class="contact-icon" viewBox="0 0 16 16" aria-hidden="true"><path d="M8 1a7 7 0 100 14A7 7 0 008 1zm0 1.5c.9 0 1.9 1.8 2.1 4.7H5.9C6.1 4.3 7.1 2.5 8 2.5zM2.6 7.2a5.6 5.6 0 012.6-4 9 9 0 00-.8 4zm0 1.6h1.8c.1 1.6.4 2.9.8 4a5.6 5.6 0 01-2.6-4zM8 13.5c-.9 0-1.9-1.8-2.1-4.7h4.2c-.2 2.9-1.2 4.7-2.1 4.7zm2.8-.3c.4-1.1.7-2.4.8-4h1.8a5.6 5.6 0 01-2.6 4zm.8-6c-.1-1.6-.4-2.9-.8-4a5.6 5.6 0 012.6 4z"/></svg>
        <span>WWW.YOUESITEGOESHERE.COM</span>
      </li>
      <li class="contact-item">
        <svg class="contact-icon" viewBox="0 0 16 16" aria-hidden="true"><path d="M1 3h14v1.2L8 9 1 4.2zM1 6l7 4.8L15 6v7H1z"/></svg>
        <span>EMAIL@DOMAINGOESHERE.COM</span>
      </li>
      <li class="contact-item">
        <svg class="contact-icon" viewBox="0 0 16 16" aria-hidden="true"><path d="M8 1a5 5 0 00-5 5c0 3.8 5 9 5 9s5-5.2 5-9a5 5 0 00-5-5zm0 7a2 2 0 110-4 2 2 0 010 4z"/></svg>
        <span>STREET NAME, ZIP CODE<br>1234, CITY</span>
      </li>
    </ul>
  </section>

  <section class="card card--back" aria-label="Business card back">
    <div class="back-band"></div>
  </section>

</main>
</body>
</html>
```